"Retire With The Harrowgate Fund" Book Cover Design

This book is 5.5 x. 8.5 in size. Not enough room for any writing on the spine either. About 100 pages, and 18,000 words max.
The Harrowgate Fund goes back to 1930. In this book, I run scenario after scenario seeing what the best strategy was for someone to Retire With The Harrowgate Fund and never run out of money. And how they MIGHT be able to use this info to build a solid retirement plan using the Harrowgate Fund for themselves.
Target Market(s)
Soon-to-be and recent middle-class, married retirees.
Industry/Entity Type
Investment Advisory
Requirements
Must have
- MUST BE EYE CATCHING!
Should not have
- No Piggy Banks or old people sitting on a beach or any yachts.

```html
<!DOCTYPE html>
<html lang="en">
<head>
<meta charset="utf-8">
<title>Retire With The Harrowgate Fund — Book Cover</title>
<link rel="stylesheet" href="https://fonts.googleapis.com/css2?family=Anton&display=swap">
<style>
  :root {
    --paper: #ffffff;
    --ink: #2b2b2c;
    --charcoal: #404040;
    --rule: #000000;
    --blue: #4096df;
    --blue-veil: rgba(74, 155, 218, 0.85);
    --blue-pale: #9fc8ea;
    --blue-soft: #94c3ec;
    --photo-deep: #15385a;
    --photo-mid: #24598a;
    --photo-light: #3b8fd3;
  }
  * { margin: 0; padding: 0; box-sizing: border-box; }
  html, body { width: 800px; height: 1200px; overflow: hidden; background: var(--paper); }
  .cover { position: relative; width: 800px; height: 1200px; background: var(--paper); overflow: hidden; }

  .title {
    position: absolute; left: 73px; top: 150px;
    font-family: "Anton", "Impact", sans-serif;
    font-weight: 400; font-size: 60px; line-height: 58.7px;
    letter-spacing: 4px; text-transform: uppercase;
    color: var(--ink);
  }
  .title span { display: block; white-space: nowrap; }

  .photo {
    position: absolute; left: 71px; top: 397px; width: 623px; height: 558px;
    background:
      radial-gradient(ellipse 22% 24% at 48% 18%, var(--photo-light) 0%, rgba(59,143,211,0) 100%),
      radial-gradient(ellipse 30% 20% at 88% 68%, rgba(59,143,211,0.8) 0%, rgba(59,143,211,0) 100%),
      linear-gradient(180deg, var(--photo-deep) 0%, var(--photo-mid) 55%, #2f70aa 100%);
  }

  .block { position: absolute; }
  .block--charcoal { left: 491px; top: 269px; width: 92px; height: 99px; background: var(--charcoal); }
  .block--veil { left: 553px; top: 312px; width: 141px; height: 151px; background: var(--blue-veil); }
  .block--base { left: 71px; top: 865px; width: 203px; height: 177px; background: var(--blue); }
  .block--tip-top { left: 669px; top: 140px; width: 25px; height: 25px; background: var(--blue-pale); }
  .block--tip-right { left: 763px; top: 648px; width: 29px; height: 31px; background: var(--blue-pale); }
  .block--dot { left: 631px; top: 847px; width: 22px; height: 22px; background: var(--blue-soft); }
  .block--tall { left: 632px; top: 976px; width: 58px; height: 91px; background: var(--blue-pale); }
  .block--small-dark { left: 382px; top: 1055px; width: 27px; height: 28px; background: var(--charcoal); }

  .rules { position: absolute; left: 0; top: 0; width: 800px; height: 1200px; pointer-events: none; }
  .rules line { stroke: var(--rule); stroke-width: 3; }
</style>
</head>
<body>
  <main class="cover">
    <h1 class="title">
      <span>Retire</span>
      <span>With The</span>
      <span>Harrowgate</span>
      <span>Fund</span>
    </h1>

    <div class="photo" role="img" aria-label="Blue-toned photo of a retired couple walking away down a tree-lined park path"></div>

    <div class="block block--charcoal"></div>
    <div class="block block--veil"></div>
    <div class="block block--base"></div>
    <div class="block block--tip-top"></div>
    <div class="block block--tip-right"></div>
    <div class="block block--dot"></div>
    <div class="block block--tall"></div>
    <div class="block block--small-dark"></div>

    <svg class="rules" viewBox="0 0 800 1200" aria-hidden="true">
      <line x1="548" y1="269" x2="676" y2="163"/>
      <line x1="305" y1="1061" x2="764" y2="677"/>
    </svg>
  </main>
</body>
</html>
```